CBD Boutique Business Card Needed

We are in need of a business card to reflect the direction of our latest products. We are a fully organic company in which our store and products are very heavy in wood and "natural" components. We decided to bring color into one of our brands and immediately knew this is where we needed to go.

We are NOT a cash grab CBD company. We could have done this wrong, slapped a label on a shit product and left it like that. I am passionate about sharing my experience with other veterans and opening a store and making it a comfortable place for others to come and see if they can have the same experience.

Target Market(s)

We are a dual market company. We do have a beauty line that will cover the costs of the majority of our business. But we also heavily cater to veterans and first responders. I am a veteran and this is how I found out about CBD. So the marketing needs to bring in our higher end beauty clientele but also be able to not put off our customers that readily need this.

Contact Information for Business Card

What we are looking for is a light, professional, boutique design that is is neither quite feminine or masculine. Attached is a picture of a store in Portland that we asked our store designer to get her inspiration from. But all natural wood and black outlines are what is mostly in there.

Attached are the following files:

Logo: An AI file with how we have our logo. I do not understand AI and have no idea why the letters are individual. The font is Adam. OLU is the logo and Tonics of Vigor is our tagline.

KM Vantage (front and back) cards I did originally found at a trade show that I absolutely loved...while it is mostly there and I would still be happy with them but it is me pretending to be you. I understand I am not and there is probably a lot wrong that all of you would see instantly and this is why I am here.

Dropper Bottle: This is our final product mock up

Water Color: I am semi flexible here. This water color is slightly different on every level of our brand. The color itself can change...we are not stuck on THIS particular one. If you happen to make a new one that is similar in style and we use it...then I will happily commission you to change the rest on our next product run. I am pretty sure you can use this statement as evidence later . =) .

But seriously, we heavily believe in pay it forward and will work with anyone here that may have a vision bigger than ours. The winner of this contest will get preferential consideration on our marketing materials (need letterhead etc. next, as well as a brochure, and website) so three more projects coming down the pipeline.

Information to use for your mockup is contained on the card images I have included. I would prefer CBD for wellness CBD for life to be more prominent. No where else on the card do we have CBD mentioned.

Font styles to use
Sans Serif

Colors

Designer to choose colors to be used in the design.

Requirements
Must have
• Double Sided
• Front: OLU logo on front of card will be raised embossed. Background is watercolor. One has been provided. Others are up for consideration. If the rest of your design is incredible and I don't like your watercolor I will just ask to swap it.
• Back: Standard information. Not stuck on anything here. I LOVE clean minimal designs. The bleed on the card I provided is a luxury...
• Font for title and OLU is Adam. Everything else I prefer san serif or as clean as possible.
Nice to have
• I Need to incorporate Naturally Nurturing somewhere on the card. Bold but not intrusive.

```html
<!DOCTYPE html>
<html lang="en">
<head>
<meta charset="utf-8">
<title>OLU – Tonics of Vigor business card</title>
<link rel="stylesheet" href="https://fonts.googleapis.com/css2?family=Montserrat:wght@300;400;500&family=Inter:wght@400&display=swap">
<style>
  :root {
    --backdrop: #ebebeb;
    --card: #ffffff;
    --ink: #1f1f1f;
    --ink-soft: #3a3a3a;
    --logo-ink: #2b2b2b;
    --teal: #3fb0c2;
    --teal-pale: #e4f3f5;
    --amber: #d98a3a;
    --amber-pale: #fbeee4;
  }
  * { margin: 0; padding: 0; box-sizing: border-box; }
  html, body { width: 1200px; height: 900px; overflow: hidden; }
  body {
    background: var(--backdrop);
    font-family: "Montserrat", sans-serif;
    color: var(--ink);
    position: relative;
  }
  .card {
    position: absolute;
    top: 140px;
    width: 405px;
    height: 620px;
    border-radius: 20px;
    background: var(--card);
    overflow: hidden;
    box-shadow: 0 1px 3px rgba(0,0,0,0.18);
  }
  .card--info { left: 164px; }
  .card--cover { left: 682px; }

  .wash { position: absolute; inset: 0; }
  .wash--faint {
    background: linear-gradient(200deg, var(--teal-pale) 0%, var(--card) 50%, var(--amber-pale) 100%);
  }
  .wash--bold {
    background: linear-gradient(200deg, var(--teal) 0%, #9cc9bf 40%, #e3a862 62%, var(--amber) 100%);
  }

  .brand { position: absolute; }
  .brand__name {
    font-family: "Montserrat", sans-serif;
    font-weight: 300;
    color: var(--logo-ink);
    line-height: 1;
    letter-spacing: 0.04em;
  }
  .brand__tagline {
    font-weight: 300;
    color: var(--ink-soft);
    letter-spacing: 0.08em;
    text-transform: uppercase;
    white-space: nowrap;
  }
  .card--info .brand { left: 37px; top: 40px; }
  .card--info .brand__name { font-size: 80px; }
  .card--info .brand__tagline { font-size: 15.5px; margin-top: 2px; }
  .card--cover .brand { left: 0; right: 0; top: 252px; text-align: center; }
  .card--cover .brand__name { font-size: 94px; }
  .card--cover .brand__tagline { font-size: 18px; margin-top: 2px; }

  .person { position: absolute; left: 38px; top: 280px; }
  .person__name {
    font-family: "Inter", sans-serif;
    font-size: 25px;
    font-weight: 400;
    letter-spacing: -0.01em;
  }
  .person__role {
    font-size: 17px;
    letter-spacing: 0.04em;
    margin-top: 8px;
  }
  .address {
    position: absolute; left: 38px; top: 378px;
    font-size: 15px; line-height: 19px; font-style: normal;
  }
  .contacts { position: absolute; left: 38px; top: 457px; list-style: none; }
  .contacts li {
    display: flex; align-items: center;
    height: 20px; margin-bottom: 12.5px;
    font-size: 15.5px;
  }
  .contacts svg { width: 18px; height: 18px; margin-right: 15px; flex: none; }
  .slogan {
    position: absolute; left: 38px; top: 572px;
    font-size: 18px; font-weight: 500; letter-spacing: 0.01em;
    color: var(--ink);
  }
</style>
</head>
<body>
  <section class="card card--info">
    <div class="wash wash--faint" role="img" aria-label="Faint teal and peach watercolor wash"></div>
    <div class="brand">
      <div class="brand__name">OLU</div>
      <div class="brand__tagline">Tonics of Vigor</div>
    </div>
    <div class="person">
      <h1 class="person__name">Dana Whitfield</h1>
      <p class="person__role">OWNER / CEO</p>
    </div>
    <address class="address">2140 N Saguaro Way Mesa,<br>AZ 85201 Suite 200</address>
    <ul class="contacts">
      <li>
        <svg viewBox="0 0 24 24" fill="none" stroke="#333" stroke-width="1.3"><path d="M5 3l4 1 1.5 4.5-2.5 1.5a12 12 0 0 0 6 6l1.5-2.5L20 15l1 4-2 2C10 21 3 14 3 5z"/></svg>
        480.555.0142
      </li>
      <li>
        <svg viewBox="0 0 24 24" fill="none" stroke="#333" stroke-width="1.3"><rect x="3" y="5" width="18" height="14"/><path d="M3 5l9 8 9-8M3 19l7-7M21 19l-7-7"/></svg>
        hello@olu.life
      </li>
      <li>
        <svg viewBox="0 0 24 24" fill="none" stroke="#222" stroke-width="1.6"><circle cx="12" cy="12" r="9"/><ellipse cx="12" cy="12" rx="4" ry="9"/><path d="M3 12h18M4.5 7.5h15M4.5 16.5h15"/></svg>
        www.olu.life
      </li>
    </ul>
    <p class="slogan">CBD for wellness&nbsp; CBD for life</p>
  </section>

  <section class="card card--cover">
    <div class="wash wash--bold" role="img" aria-label="Watercolor wash in teal and amber orange"></div>
    <div class="brand">
      <div class="brand__name">OLU</div>
      <div class="brand__tagline">Tonics of Vigor</div>
    </div>
  </section>
</body>
</html>
```